Quartz Pivot Business Card Design

I need a 2-sided business card for my computer engineering consulting company. The card is expected to convey a message of cutting edge forward thinking, and boldnes. I would like the card to be memorable and stand-out on a desk. The card should be bold, modern, clean, and highly professional. I am a big fan of watermarks/shadows and other intersting but restrained uses of the logo. The card can be a shape other than the traditional rectangle. Perhaps a rectangle with rounded edges. All I ask is the card be able to fit into a standard wallet. I will supply two logos, one with a red background, and one with a black background. Please feel free to work with both of these logos.
Updates

Hi all, thank you for your submissions. I will post the original vector file later today. Thank you for your patience.

Regards,

Martin

Target Market(s)

Engineering Buyers, Vice Presidents and Directors

Industry/Entity Type

Computer

Requirements
Must have
• 2 sides

```html
<!DOCTYPE html>
<html lang="en">
<head>
<meta charset="utf-8">
<title>Quartz Pivot Works – Business Card</title>
<link href="https://fonts.googleapis.com/css2?family=Open+Sans:wght@400;600;700&display=swap" rel="stylesheet">
<style>
  :root {
    --backdrop: #e4e4e4;
    --brand-red: #c4222b;
    --brand-red-deep: #a81b23;
    --ink-black: #0c0c0c;
    --ink-dark: #333333;
    --steel-grey: #8a8a8a;
    --panel-grey: #3a3a3a;
    --text-light: #e6e6e6;
    --text-soft: #cfcfcf;
    --white: #ffffff;
  }
  * { box-sizing: border-box; margin: 0; padding: 0; }
  html, body { width: 1200px; height: 880px; overflow: hidden; }
  body {
    background: var(--backdrop);
    font-family: "Open Sans", Arial, sans-serif;
  }
  .canvas {
    width: 1200px; height: 880px;
    display: flex; flex-direction: column;
    align-items: center; justify-content: center; gap: 40px;
  }
  .card {
    position: relative;
    width: 680px; height: 388px;
    border-radius: 26px;
    overflow: hidden;
    box-shadow: 0 6px 18px rgba(0,0,0,0.25);
  }

  /* Front side */
  .card--front {
    background: var(--brand-red);
    display: flex; align-items: center; justify-content: center;
  }
  .front-logo { display: flex; flex-direction: column; align-items: center; }
  .front-logo__row { display: flex; align-items: center; gap: 16px; }
  .front-logo__mark { width: 40px; height: 40px; background: var(--ink-dark); }
  .front-logo__name {
    font-size: 46px; font-weight: 600; letter-spacing: 1px;
    color: var(--ink-dark); text-transform: uppercase; white-space: nowrap;
  }
  .front-logo__tagline {
    margin-top: 4px;
    font-size: 18px; letter-spacing: 7px;
    color: #7a7a7a; text-transform: uppercase; white-space: nowrap;
  }

  /* Back side */
  .card--back { background: var(--ink-black); }
  .back-art { position: absolute; inset: 0; }
  .back-logo {
    position: absolute; left: 330px; top: 100px;
    white-space: nowrap;
  }
  .back-logo__name {
    font-size: 24px; font-weight: 600; letter-spacing: 0.5px; line-height: 32px;
    color: var(--brand-red); text-transform: uppercase;
  }
  .back-logo__suffix {
    font-size: 11px; letter-spacing: 2px; color: var(--steel-grey);
    margin-left: 6px;
  }
  .back-logo__tagline {
    margin-top: 2px;
    font-size: 12px; letter-spacing: 4px;
    color: var(--steel-grey); text-transform: uppercase;
  }
  .contact-panel {
    position: absolute; left: 300px; top: 190px;
    width: 380px; height: 150px;
    background: var(--panel-grey);
    padding: 12px 22px;
    color: var(--text-light);
  }
  .contact-panel__name {
    font-size: 22px; font-weight: 400; color: var(--white);
    line-height: 30px; margin-bottom: 6px;
  }
  .contact-list { list-style: none; }
  .contact-list__item {
    display: flex; align-items: center; gap: 9px;
    font-size: 12.5px; line-height: 20px; color: var(--text-soft);
  }
  .contact-list__icon { width: 13px; height: 13px; fill: var(--text-soft); }
  .contact-panel__web {
    position: absolute; left: 22px; bottom: 10px;
    font-size: 15px; line-height: 20px; color: #d8d8d8;
  }
</style>
</head>
<body>
<main class="canvas">

  <section class="card card--front" aria-label="Card front">
    <div class="front-logo">
      <div class="front-logo__row">
        <span class="front-logo__mark"></span>
        <span class="front-logo__name">Quartz Pivot Works</span>
      </div>
      <span class="front-logo__tagline">Engineering Beyond Limits</span>
    </div>
  </section>

  <section class="card card--back" aria-label="Card back">
    <svg class="back-art" viewBox="0 0 680 388" width="680" height="388">
      <polygon points="0,0 250,0 120,388 0,388" fill="var(--brand-red)"/>
      <polygon points="250,0 262,0 132,388 120,388" fill="var(--white)"/>
      <circle cx="140" cy="150" r="110" fill="var(--ink-black)" role="img" aria-label="Red figure silhouette set against a black disc"/>
      <polygon points="600,0 680,0 680,18 600,18" fill="var(--brand-red-deep)"/>
      <polygon points="600,370 680,370 680,388 600,388" fill="var(--steel-grey)"/>
    </svg>

    <div class="back-logo">
      <div class="back-logo__name">Quartz Pivot Works<span class="back-logo__suffix">LTD</span></div>
      <div class="back-logo__tagline">Engineering Beyond Limits</div>
    </div>

    <div class="contact-panel">
      <div class="contact-panel__name">Elena Marsh</div>
      <ul class="contact-list">
        <li class="contact-list__item">
          <svg class="contact-list__icon" viewBox="0 0 16 16"><path d="M4 1l3 3-2 2c1 2 3 4 5 5l2-2 3 3-2 2C7 14 2 9 2 3z"/></svg>
          555.014.2290
        </li>
        <li class="contact-list__item">
          <svg class="contact-list__icon" viewBox="0 0 16 16"><rect x="4" y="1" width="8" height="4"/><rect x="1" y="6" width="14" height="6"/><rect x="4" y="10" width="8" height="5"/></svg>
          555.018.3417
        </li>
        <li class="contact-list__item">
          <svg class="contact-list__icon" viewBox="0 0 16 16"><path d="M1 3h14v10H1z M1 3l7 6 7-6" fill="none" stroke="#cfcfcf" stroke-width="1.5"/></svg>
          info@quartzpivotworks.com
        </li>
      </ul>
      <div class="contact-panel__web">www.quartzpivotworks.com</div>
    </div>
  </section>

</main>
</body>
</html>
```